Promotional Flyer for "Ventaro events" with LOGO DESIGN

I am developing my own start-up company which is organising and managing exclusive and luxury events in Vienna, London, and Venice. Elegant promotional flyer should introduce and promote my company to a broad spectrum of high level clients; both online and by regular hardcopy post. This flyer should reflect the highest level of elegance, professionalism, creativity, sophistication, and exclusivity as well as irradiating a feeling of child like joy . I want the flyer to be two sided or folded, but did not find that version. It should be including the photo from the main page of the site "www.ventaro-events.example". Text should contain the following :
Creative ideas and event concept
Unique venue selection
Complete planning and coordination
First class catering
Professional photography and video productions ---
--------------------------------------------------------------------
1.Enchant the unenchantable
2. we materialise your innermost dreams into trend setting entertainment and unique celebration of any occasion
------------------------------------------------------------------------
You can take ideas from any photo on my website, I also add some additional photos
I am available via e-mail or phone +390000000000 /+440000000000. Thank you.

Target Market(s)

high level discreet and the discerning client with taste, well travelled already spoiled

Industry/Entity Type

Event Planning

Font styles to use
Sans Serif

Colors
ffffff
fffbf0

Requirements
Must have
• unexpected simlicity, be extremely different from all what is there on the market
Should not have
• eye catching and memorable yet not too busy

```html
<!DOCTYPE html>
<html lang="en">
<head>
<meta charset="utf-8">
<title>Ventaro Events Flyer</title>
<link href="https://fonts.googleapis.com/css2?family=Montserrat:wght@300;700&display=swap" rel="stylesheet">
<style>
  :root {
    --ink: #ffffff;
    --cream: #fffbf0;
    --cork-light: #a8865e;
    --cork-mid: #7a5a3a;
    --cork-dark: #3f2c1c;
    --band: rgba(40, 28, 18, 0.55);
  }
  html, body {
    margin: 0;
    padding: 0;
    width: 1200px;
    height: 1200px;
    overflow: hidden;
    background: #ffffff;
  }
  .flyer {
    position: relative;
    width: 1200px;
    height: 1200px;
    border-radius: 14px;
    overflow: hidden;
    font-family: "Montserrat", sans-serif;
    color: var(--ink);
  }
  .backdrop {
    position: absolute;
    inset: 0;
    background:
      radial-gradient(circle at 80% 55%, #8a6a48 0%, rgba(90,64,40,0) 32%),
      radial-gradient(circle at 20% 75%, #9a7a55 0%, rgba(90,64,40,0) 40%),
      linear-gradient(160deg, var(--cork-mid) 0%, var(--cork-light) 45%, var(--cork-mid) 70%, var(--cork-dark) 100%);
  }
  .header-band {
    position: absolute;
    left: 0;
    top: 0;
    width: 100%;
    height: 282px;
    background: var(--band);
  }
  .brand-name {
    position: absolute;
    top: 26px;
    width: 100%;
    text-align: center;
    margin: 0;
    font-size: 110px;
    font-weight: 700;
    letter-spacing: 1px;
    line-height: 1;
  }
  .rule {
    position: absolute;
    left: 121px;
    top: 166px;
    width: 958px;
    height: 8px;
    background: var(--ink);
  }
  .tagline {
    position: absolute;
    top: 196px;
    width: 100%;
    text-align: center;
    margin: 0;
    font-size: 49px;
    font-weight: 700;
    letter-spacing: 1px;
    line-height: 62px;
  }
  .services {
    position: absolute;
    left: 68px;
    top: 289px;
    margin: 0;
    padding: 0;
    list-style: none;
  }
  .services li {
    font-size: 48px;
    font-weight: 300;
    height: 90.8px;
    line-height: 90.8px;
    letter-spacing: 1px;
    white-space: nowrap;
  }
  .footer {
    position: absolute;
    top: 1120px;
    width: 100%;
    text-align: center;
    line-height: 1.2;
  }
  .site {
    font-size: 22px;
    font-weight: 700;
    letter-spacing: 0.5px;
  }
  .motto {
    font-size: 20px;
    font-weight: 300;
    letter-spacing: 0.5px;
  }
</style>
</head>
<body>
  <main class="flyer">
    <div class="backdrop" role="img" aria-label="Photograph of wine corks scattered around an antique brass compass"></div>
    <div class="header-band"></div>
    <h1 class="brand-name">VENTARO EVENTS</h1>
    <div class="rule"></div>
    <p class="tagline">EXCLUSIVE • EXTRAORDINARY • EXOTIC</p>
    <ul class="services">
      <li>- CREATIVE IDEAS &amp; EVENT CONCEPT</li>
      <li>- UNIQUE VENUE SELECTION</li>
      <li>- COMPLETE PLANNING &amp; COORDINATION</li>
      <li>- EFFICIENT BUDGET MANAGEMENT</li>
      <li>- FIRST CLASS CATERING</li>
      <li>- PROFESSIONAL PHOTOGRAPHY &amp; VIDEO</li>
      <li>- AMAZING DECORATION &amp; DESIGN</li>
      <li>- LIVELY ENTERTAINMENT</li>
      <li>- PROFESSIONAL PHOTOGRAPHY &amp; VIDEO</li>
    </ul>
    <footer class="footer">
      <div class="site">VENTARO-EVENTS.EXAMPLE</div>
      <div class="motto">ENCHANT THE UNENCHANTABLE</div>
    </footer>
  </main>
</body>
</html>
```